Visitenkarten-Design für Personal-Training
Zielgruppe
Kai Brenner Personal Training.
Personaltraining für Bürotätige / leitende Positionen.
Rücken- und Haltungstraining.
Zielgruppe: Herren mittleren Alters, gehobene Klasse.
Aufgabenstellung
Schlicht, elegant, hochwertig
Gerne Logo eingearbeitet.
Schwarz / Gold / Weiß

```html
<!DOCTYPE html>
<html lang="de">
<head>
<meta charset="utf-8">
<title>Kai Brenner Personal Training – Visitenkarte</title>
<link rel="stylesheet" href="https://fonts.googleapis.com/css2?family=Roboto+Slab:wght@400;700&display=swap">
<style>
  :root {
    --stage: #ebebea;
    --paper: #ffffff;
    --ink: #1b1b1b;
    --gold: #b39a34;
    --night: #1e1a17;
  }
  * { margin: 0; padding: 0; box-sizing: border-box; }
  html, body { width: 1200px; height: 800px; overflow: hidden; }
  body {
    background: var(--stage);
    font-family: "Roboto Slab", Georgia, serif;
    position: relative;
  }
  .card {
    position: absolute;
    top: 225px;
    width: 540px;
    height: 350px;
  }
  .card--front { left: 30px; background: var(--paper); }
  .card--back { left: 630px; background: var(--night); }

  .brand {
    color: var(--gold);
    font-weight: 700;
    line-height: 1;
  }
  .brand__tagline { display: block; font-size: 10px; letter-spacing: 0.06em; text-transform: uppercase; }
  .brand__mark { display: block; font-size: 50px; letter-spacing: 0.02em; }

  .card--front .brand { position: absolute; top: 34px; right: 40px; text-align: left; }
  .card--front .brand__tagline { margin-bottom: 4px; }

  .person { position: absolute; left: 40px; top: 150px; }
  .person__name { color: var(--gold); font-weight: 700; font-size: 19px; }
  .person__role { color: var(--ink); font-size: 18px; margin-top: 2px; }

  .divider { position: absolute; left: 40px; right: 40px; top: 212px; height: 2px; background: var(--gold); }

  .address { position: absolute; left: 60px; top: 236px; color: var(--ink); font-size: 13px; line-height: 1.45; font-style: normal; }
  .contact { position: absolute; right: 40px; top: 236px; color: var(--ink); font-size: 13px; line-height: 1.45; text-align: left; list-style: none; }

  .card--back .brand { position: absolute; left: 50%; top: 50%; transform: translate(-50%, -50%); text-align: left; }
  .card--back .brand__tagline { font-size: 13px; margin-bottom: 6px; }
  .card--back .brand__mark { font-size: 78px; }
</style>
</head>
<body>
  <section class="card card--front" aria-label="Visitenkarte Vorderseite">
    <div class="brand">
      <span class="brand__tagline">Kai Brenner Personal Training</span>
      <span class="brand__mark">KBPT</span>
    </div>
    <div class="person">
      <p class="person__name">Jonas Falkner</p>
      <p class="person__role">Geschäftsfuhrer</p>
    </div>
    <div class="divider"></div>
    <address class="address">
      Your Addres 1<br>
      Your City Zip Code 106
    </address>
    <ul class="contact">
      <li>+41 22 480 16 30</li>
      <li>kbpt-training.de</li>
      <li>mail@kbpt-training.de</li>
    </ul>
  </section>

  <section class="card card--back" role="img" aria-label="Visitenkarte Rückseite: dunkler Grund mit feinem Hantelscheiben-Muster und Markenname">
    <div class="brand">
      <span class="brand__tagline">Kai Brenner Personal Training</span>
      <span class="brand__mark">KBPT</span>
    </div>
  </section>
</body>
</html>
```